HIgh-end jewelry designer needs a business card design

I need a business card design for the ecclectic & rather expensive jewelry designs. My approach to my work is to combine very old jewelry offset with contemporary items. I enjoy the idea of legacy as well as repurposing finely crafted items that are not possible to create any longer. My desire is to celebrate the past in a contemporary & funky way. The name of my business is MERIVALE. I see my business card design as simple & yet enigmatic as possible. In the end... clean, simple & understated is the look I am after. Thank you for your consideration...

Target Market(s)

I will use this business card for the trade as well as customers

Industry/Entity Type

Business

Contact Information for Business Card

Corinne Halvard Owner/Designer 555-274-8163

Requirements
Must have
• Clean & simple sophisticated design using the word "Merivalle" as the logo. I like the idea of a play on the word itself, perhaps even using different fonts (i.e.: a bold helvetica combined with a lovely script). I'm afraid to say more because I don't want to limit creative input. Gosh, sometimes it's ok to break the rules!
Nice to have
• In my mind, I have imagined this business card to be simple, using my company name "Merivale" in a playful yet sophisticated manner. I believe that doing something beautifully simple can be a true challenge. I have imagined something with just black & white, however I am open to ideas... after all that's why I'm here!
Should not have
• As Mozart once said... "It has too many notes!" I know I'm being silly, but I don't want it to be complicated or overly ornate.

```html
<!DOCTYPE html>
<html lang="en">
<head>
<meta charset="utf-8">
<title>Merivale — Business Card</title>
<link rel="stylesheet" href="https://fonts.googleapis.com/css2?family=Almendra:wght@400;700&display=swap">
<style>
  :root {
    --ink: #0a0a0a;
    --paper: #ffffff;
  }
  html, body {
    margin: 0;
    padding: 0;
    overflow: hidden;
    background: var(--paper);
  }
  .card {
    position: relative;
    width: 702px;
    height: 1200px;
    background: var(--paper);
    overflow: hidden;
    font-family: "Almendra", Georgia, serif;
  }
  .card__wedge {
    position: absolute;
    inset: 0;
    width: 702px;
    height: 1200px;
  }
  .card__wedge polygon {
    fill: var(--ink);
  }
  .brand {
    position: absolute;
    left: 352px;
    top: 582px;
    margin: 0;
    font-size: 62px;
    font-weight: 700;
    line-height: 1;
    color: var(--paper);
    letter-spacing: 0.5px;
  }
  .contact {
    position: absolute;
    right: 58px;
    top: 890px;
    margin: 0;
    text-align: right;
    color: var(--paper);
    font-style: normal;
  }
  .contact__name {
    display: block;
    font-size: 46px;
    font-weight: 700;
    line-height: 1.2;
  }
  .contact__role {
    display: block;
    font-size: 32px;
    font-weight: 700;
    line-height: 1.7;
  }
  .contact__phone {
    display: block;
    font-size: 37px;
    font-weight: 700;
    line-height: 1.5;
  }
  .contact__email {
    display: block;
    font-size: 34px;
    font-weight: 700;
    line-height: 1.5;
  }
</style>
</head>
<body>
  <main class="card">
    <svg class="card__wedge" viewBox="0 0 702 1200" aria-hidden="true">
      <polygon points="603,0 702,0 702,1200 72,1200"/>
    </svg>

    <h1 class="brand">Merivale</h1>

    <address class="contact">
      <span class="contact__name">Corinne Halvard</span>
      <span class="contact__role">Owner/Designer</span>
      <span class="contact__phone">555-274-8163</span>
      <span class="contact__email">chalvard1@merivale.co</span>
    </address>
  </main>
</body>
</html>
```